business card for LWR pty ltd

We require a business card that stands out . I have included our company flyer and would like the services listed to be put on the card so when we Give out the cards to customers they have an idea of services we provide. need the winning design to be in editable photo shop format, editable iMac pages format or editable windows publisher format, so that I can enter in names, email addresses, phone numbers etc myself. I have included a pdf documents of info / items needed on the card to use as reference please.
Updates

need more submissions

Need extra days to review

Sick

Target Market(s)

new customers

Contact Information for Business Card

details are on attached business card requirements file

Requirements
Must have
• I have attached a list of must haves

```html
<!DOCTYPE html>
<html lang="en">
<head>
<meta charset="UTF-8">
<title>LWR pty ltd — Business Card</title>
<link href="https://fonts.googleapis.com/css2?family=Montserrat:wght@600;700&family=Michroma&display=swap" rel="stylesheet">
<style>
  :root {
    --backdrop: #8e8e8e;
    --card-black: #0c0c0c;
    --card-charcoal: #1d1d1d;
    --text-silver: #d9d9d9;
    --text-muted: #a4a4a4;
    --bullet-grey: #8a8a8a;
    --logo-grey: #9a9a9a;
    --sand-light: #c99a6a;
    --sand-dark: #8a5a34;
    --rule: #5a5a5a;
  }
  * { box-sizing: border-box; margin: 0; padding: 0; }
  html, body { width: 1200px; height: 1200px; overflow: hidden; }
  body {
    background: var(--backdrop);
    display: flex;
    flex-direction: column;
    align-items: center;
    justify-content: center;
    gap: 40px;
    font-family: "Montserrat", Arial, sans-serif;
  }
  .card {
    width: 900px;
    height: 540px;
    position: relative;
    overflow: hidden;
    background: radial-gradient(ellipse at 40% 30%, var(--card-charcoal), var(--card-black) 75%);
    box-shadow: 0 8px 24px rgba(0,0,0,0.35);
  }

  /* Back: services */
  .services {
    position: absolute;
    left: 70px;
    top: 62px;
    list-style: none;
  }
  .services li {
    color: var(--text-silver);
    font-weight: 700;
    font-size: 25px;
    letter-spacing: 0.5px;
    line-height: 38px;
    text-transform: uppercase;
    padding-left: 30px;
    position: relative;
  }
  .services li::before {
    content: "";
    position: absolute;
    left: 0;
    top: 13px;
    width: 13px;
    height: 13px;
    background: var(--bullet-grey);
  }
  .services li .second-line { display: block; line-height: 28px; }
  .back-brand {
    position: absolute;
    right: 60px;
    top: 40px;
    writing-mode: vertical-rl;
    font-weight: 700;
    font-size: 190px;
    line-height: 1;
    color: var(--logo-grey);
    letter-spacing: 4px;
  }

  /* Front: identity */
  .front-brand {
    position: absolute;
    left: 0; right: 0;
    top: 36px;
    text-align: center;
    font-weight: 700;
    font-size: 120px;
    line-height: 1;
    color: var(--logo-grey);
    letter-spacing: 6px;
    z-index: 2;
  }
  .fleet-photo {
    position: absolute;
    left: 0; right: 0;
    top: 150px;
    height: 215px;
    background: linear-gradient(180deg, rgba(12,12,12,1) 0%, rgba(40,36,34,0.9) 22%, var(--sand-dark) 55%, var(--sand-light) 100%);
  }
  .identity {
    position: absolute;
    left: 0; right: 0;
    top: 382px;
    text-align: center;
    font-family: "Michroma", "Arial Black", sans-serif;
    color: var(--text-silver);
  }
  .person { display: flex; justify-content: center; align-items: baseline; gap: 16px; }
  .person-name { font-size: 28px; letter-spacing: 2px; line-height: 38px; }
  .person-title { font-size: 14px; letter-spacing: 3px; color: var(--text-muted); }
  .name-rule { width: 320px; height: 1px; background: var(--rule); margin: 6px auto 10px; }
  .contact-line {
    font-size: 15px;
    letter-spacing: 1.5px;
    line-height: 25px;
    display: flex;
    justify-content: center;
    align-items: center;
    gap: 8px;
  }
  .contact-line .divider { color: var(--text-muted); margin: 0 6px; }
  .icon { width: 15px; height: 15px; fill: none; stroke: var(--text-muted); stroke-width: 2; }
</style>
</head>
<body>

<section class="card card-back" aria-label="Card back: services">
  <ul class="services">
    <li>Over size loads/ hot shot loads</li>
    <li>Heavy vehicle recovery serivices</li>
    <li>Portable water deliveries</li>
    <li>Road building / maintenance</li>
    <li>Earthworks</li>
    <li>Sand &amp; metal supply &amp; cartage</li>
    <li>Road train tippers</li>
    <li>Road train tankers</li>
    <li>Road train flat tops</li>
    <li>Drop deck trailers</li>
    <li>Mine site accredited<span class="second-line">equipment &amp; operators</span></li>
  </ul>
  <div class="back-brand">LWR</div>
</section>

<section class="card card-front" aria-label="Card front: contact details">
  <div class="front-brand">LWR</div>
  <div class="fleet-photo" role="img" aria-label="Photo of a road train with tipper trailers on red desert sand"></div>
  <div class="identity">
    <div class="person">
      <span class="person-name">DANIEL REEVE</span>
      <span class="person-title">DIRECTOR</span>
    </div>
    <div class="name-rule"></div>
    <p class="contact-line">LOT 444 EXAMPLE ADDRESS AUSTRALIA</p>
    <p class="contact-line">
      <svg class="icon" viewBox="0 0 24 24"><path d="M5 3h4l2 5-2.5 1.5a11 11 0 0 0 6 6L16 13l5 2v4a2 2 0 0 1-2 2A17 17 0 0 1 3 5a2 2 0 0 1 2-2z"/></svg>
      000 444 000
      <span class="divider">|</span>
      <svg class="icon" viewBox="0 0 24 24"><rect x="3" y="5" width="18" height="14"/><path d="M3 5l9 8 9-8"/></svg>
      EMAIL@LWRHAULAGE.COM.AU
    </p>
    <p class="contact-line">
      <svg class="icon" viewBox="0 0 24 24"><circle cx="12" cy="12" r="9"/><path d="M3 12h18M12 3a14 14 0 0 1 0 18M12 3a14 14 0 0 0 0 18"/></svg>
      WWW.WEBSITEADDRESS.COM
    </p>
  </div>
</section>

</body>
</html>
```